Improved Business Card, Government Contracting

We are looking to update the design of our business cards. We would like to create a template that can be used for future employees and easy to update.

Halvorsen Advisory Partners, LLC is a Service Disabled Veteran Owned Small Business with headquarters located in Leavenworth, KS. Our current website is www.hapteam.com. We have contracts in KS and VA with expansion opportunities in various other states. Our primary line of work is within government contracting and providing consulting services to various organizations within the Bureau of Frontier Works. We would like to project a professional image of our company that is consistent with the industry. Provided are previous versions of our business card template that shows our logo as well. We would like to make sure the information on the cards are easily noticeable .

Target Market(s)

Government Officials
Fellow Small Business Contractors
Large Business Contractors (ex. TRUX, Keswell Barnaby, Pryde Okonjo Whitcombe)

Industry/Entity Type

Business

Contact Information for Business Card

Dale Fenwick
Office Manager
Halvorsen Advisory Partners
Ph: 913.555.0172
Email: d.fenwick@hapteam.us
www.hapteam.com

Requirements
Must have
• The business mailing address is:
• 31842 204th Lane
• Leavenworth, KS 66099
Nice to have
• Embossed lettering

```html
<!DOCTYPE html>
<html lang="en">
<head>
<meta charset="utf-8">
<title>Halvorsen Advisory Partners — Business Card</title>
<link rel="stylesheet" href="https://fonts.googleapis.com/css2?family=Carlito:wght@400;700&display=swap">
<style>
  :root {
    --bg: #e9e6e1;
    --card-blue: #2e3192;
    --brand-yellow: #f7ec3a;
    --ink-black: #050505;
    --ink-white: #ffffff;
    --wave-blue: #2b2f8f;
    --wave-yellow: #fbf26a;
  }
  * { box-sizing: border-box; margin: 0; padding: 0; }
  html, body {
    width: 1200px; height: 900px; overflow: hidden;
    background: var(--bg);
    font-family: "Carlito", "Calibri", sans-serif;
  }
  .canvas {
    position: relative; width: 1200px; height: 900px;
  }
  .card {
    position: absolute; left: 290px; width: 620px; height: 354px;
    overflow: hidden;
    box-shadow: 0 10px 24px rgba(0,0,0,.25);
  }
  /* Front */
  .card--front { top: 70px; background: var(--card-blue); color: var(--brand-yellow); }
  .front__brand {
    position: absolute; top: 82px; left: 0; right: 0;
    display: flex; align-items: center; justify-content: center; gap: 14px;
    font-weight: 700; font-size: 36px; letter-spacing: .3px;
  }
  .front__brand-square { width: 22px; height: 22px; background: var(--brand-yellow); }
  .front__services {
    position: absolute; top: 158px; left: 0; right: 0;
    list-style: none; text-align: center;
    font-size: 21px; line-height: 1.2;
  }
  /* Back */
  .card--back { top: 476px; background: var(--ink-black); color: var(--ink-white); }
  .back__contact { position: absolute; top: 40px; left: 44px; }
  .back__name { color: var(--brand-yellow); font-weight: 700; font-size: 24px; line-height: 1.1; }
  .back__title { font-size: 20px; line-height: 1.2; margin-bottom: 14px; }
  .back__lines { list-style: none; font-size: 20px; line-height: 1.25; }
  .back__lines li { display: flex; align-items: center; gap: 8px; }
  .back__lines svg { width: 16px; height: 16px; flex: none; }
  .back__address { margin-top: 16px; font-size: 20px; line-height: 1.25; }
  .back__brand {
    position: absolute; right: 40px; top: 168px;
    display: flex; align-items: center; gap: 12px;
    color: var(--brand-yellow); font-size: 24px; font-weight: 400; letter-spacing: .5px;
  }
  .back__brand-square { width: 18px; height: 18px; background: var(--brand-yellow); }
  .back__wave { position: absolute; left: 0; bottom: 0; width: 620px; height: 110px; }
</style>
</head>
<body>
<main class="canvas">
  <section class="card card--front" aria-label="Card front">
    <div class="front__brand">
      <span class="front__brand-square"></span>
      <span>Halvorsen Advisory Partners</span>
    </div>
    <ul class="front__services">
      <li>Software &amp; Systems Engineering</li>
      <li>Decision Analysis &amp; Process Improvement</li>
      <li>Program &amp; Budget Analysis</li>
      <li>Command and Control</li>
      <li>Program Management</li>
    </ul>
  </section>

  <section class="card card--back" aria-label="Card back">
    <div class="back__contact">
      <p class="back__name">Dale Fenwick</p>
      <p class="back__title">Office Manager</p>
      <ul class="back__lines">
        <li>
          <svg viewBox="0 0 16 16" aria-hidden="true"><path fill="#f7ec3a" d="M3 2h3l1 4-2 1a9 9 0 0 0 4 4l1-2 4 1v3a2 2 0 0 1-2 2A12 12 0 0 1 1 4a2 2 0 0 1 2-2z"/></svg>
          <span>913.555.0172</span>
        </li>
        <li>
          <svg viewBox="0 0 16 16" aria-hidden="true"><rect x="1" y="3" width="14" height="10" fill="#f7ec3a"/><path d="M1 3l7 6 7-6" fill="none" stroke="#050505" stroke-width="1.4"/></svg>
          <span>d.fenwick@hapteam.us</span>
        </li>
        <li>
          <svg viewBox="0 0 16 16" aria-hidden="true"><circle cx="8" cy="8" r="6.5" fill="none" stroke="#f7ec3a" stroke-width="1.5"/><ellipse cx="8" cy="8" rx="2.8" ry="6.5" fill="none" stroke="#f7ec3a" stroke-width="1.2"/><path d="M1.5 8h13M2.5 5h11M2.5 11h11" stroke="#f7ec3a" stroke-width="1.1"/></svg>
          <span>www.hapteam.com</span>
        </li>
      </ul>
      <p class="back__address">31842 204th Lane<br>Leavenworth, KS 66099</p>
    </div>
    <div class="back__brand">
      <span class="back__brand-square"></span>
      <span>Halvorsen Advisory Partners</span>
    </div>
    <svg class="back__wave" viewBox="0 0 620 110" preserveAspectRatio="none" aria-hidden="true">
      <path d="M0 40 C120 20 220 25 320 45 C430 68 530 62 620 50 L620 110 L0 110 Z" fill="var(--wave-blue)"/>
      <path d="M0 48 C120 28 220 34 320 58 C430 84 530 80 620 72 L620 110 L0 110 Z" fill="var(--wave-yellow)"/>
    </svg>
  </section>
</main>
</body>
</html>
```